TidePost RV/Boat/Auto Storage

Front page for web site. Looking for a modern, clean design. Want rotating photo section (see attached) and all components similar to this web site, BUT NOT THE SAME:
https://www.marlowdepot.example/

This is a fully enclosed, for lease project. They are not condominiums for sale, or "self-storage" units. Logo and sample images are attached for your use.

Target Market(s)

Affluent customers who have high-end RV's (main focus), boats ,or automobiles.

Industry/Entity Type

Commercial real estate.

Coding

Coded - Design and coding required

Number of Pages Required

1 page

```html
<!DOCTYPE html>
<html lang="en">
<head>
<meta charset="utf-8">
<title>TidePost RV/Boat/Auto Storage</title>
<link href="https://fonts.googleapis.com/css2?family=Bebas+Neue&family=Montserrat:wght@400;500;600;700&display=swap" rel="stylesheet">
<style>
:root{
  --navy:#0f3d8c;
  --navy-dark:#0a2f6e;
  --gold:#f6b21b;
  --ink:#1c1c1c;
  --muted:#555b66;
  --pale:#eef4fc;
  --line:#c9d6ea;
  --white:#ffffff;
}
*{box-sizing:border-box;margin:0;padding:0}
html,body{width:1200px;height:5119px;overflow:hidden}
body{font-family:"Montserrat",sans-serif;color:var(--ink);background:var(--white);position:relative}
.display{font-family:"Bebas Neue",sans-serif;font-weight:400;letter-spacing:.5px;color:var(--ink)}
.eyebrow{font-size:13px;color:var(--navy);font-weight:500}
.center{text-align:center}
.lead{font-size:11.5px;line-height:17px;color:#333}
.btn{display:inline-flex;align-items:center;justify-content:center;height:36px;padding:0 34px;font-size:11px;font-weight:700;text-transform:uppercase;border-radius:3px;white-space:nowrap}
.btn-gold{background:var(--gold);color:#1b1b1b}
.btn-navy{background:var(--navy);color:var(--white)}
.btn-outline{border:1.5px solid var(--white);color:var(--white);background:var(--navy)}
section,footer{position:relative;width:1200px}

/* top bar + nav */
.topbar{height:24px;background:var(--navy-dark);color:#e8eef8;font-size:10px;display:flex;align-items:center;justify-content:center;gap:4px}
.topbar b{color:var(--gold);font-weight:600}
.topbar .accent{color:var(--gold)}
.nav{height:64px;display:flex;align-items:center;padding:0 100px;border-bottom:1px solid #eee}
.brand{display:flex;align-items:center;gap:8px;font-size:15px;font-weight:700;color:var(--navy)}
.brand-mark{width:18px;height:18px;border-radius:50%;background:var(--gold)}
.nav-links{display:flex;gap:44px;margin-left:auto;margin-right:62px;font-size:12px;font-weight:500}
.nav-links .on{color:var(--gold);position:relative}
.nav-links .on:after{content:"";position:absolute;left:0;right:0;bottom:-8px;height:2px;background:var(--gold)}
.nav .btn{height:38px;padding:0 22px}

/* hero */
.hero{height:524px;overflow:hidden}
.hero-photo{position:absolute;inset:0;background:linear-gradient(180deg,#3d4a57 0%,#5e7183 38%,#7b8fa2 55%,#2c5577 70%,#143a5c 100%)}
.hero-photo:after{content:"";position:absolute;inset:0;background:linear-gradient(90deg,rgba(10,20,35,.55) 0%,rgba(10,20,35,.15) 55%,rgba(0,0,0,0) 100%)}
.hero-body{position:absolute;left:100px;top:137px;color:var(--white)}
.hero-body .eyebrow{color:var(--gold);font-size:13px}
.hero-body h1{color:var(--white);font-size:46px;line-height:48px;margin-top:18px}
.hero-body p{font-size:11.5px;margin-top:14px}
.hero-body .actions{display:flex;gap:10px;margin-top:20px}
.dots{position:absolute;left:45px;top:234px;display:flex;flex-direction:column;gap:8px}
.dots span{width:11px;height:11px;border:1.5px solid var(--white);border-radius:50%}
.dots span.on{background:var(--white);box-shadow:inset 0 0 0 2px #4b5b6b}

/* why choose */
.why{height:418px;padding-top:56px}
.why h2{font-size:33px;margin-top:10px}
.why .lead{margin-top:12px}
.features{display:flex;gap:15px;margin:36px 100px 0}
.feature{width:188px;height:158px;border:1.5px solid #9fb7dd;border-radius:4px;text-align:center;padding-top:14px;box-shadow:0 3px 8px rgba(15,61,140,.12)}
.feature svg{width:36px;height:36px}
.feature h3{font-size:14px;font-weight:500;line-height:17px;margin-top:8px;color:#222}
.feature p{font-size:9px;line-height:12px;color:#555;margin:8px 14px 0}

/* about */
.about{height:438px;display:flex;background:var(--pale)}
.about-photo{width:600px;height:438px;background:linear-gradient(180deg,#9fb8cf 0%,#5f7a63 40%,#2f4a2e 70%,#4d5a3c 100%)}
.about-body{padding:90px 0 0 46px;width:600px}
.about-body h2{font-size:33px;margin-top:8px}
.about-body p{font-size:11px;line-height:16px;color:#333;margin-top:14px;width:460px}
.about-body .btn{margin-top:20px;width:204px}

/* services */
.services{height:642px;padding-top:72px}
.services h2{font-size:33px;margin-top:10px}
.services .lead{margin-top:12px}
.service-grid{display:flex;gap:16px;margin:36px 100px 0}
.service{width:323px;text-align:center}
.service .photo{height:218px;border-radius:4px}
.service h3{font-size:20px;font-weight:500;margin-top:16px}
.service p{font-size:9.5px;line-height:13px;color:#444;margin:10px 6px 0}
.pair{display:flex;justify-content:center;gap:10px;margin-top:32px}

/* reviews */
.reviews{height:530px;padding-top:62px;background:linear-gradient(180deg,#e6edf7,#dfe7f3)}
.reviews h2{font-size:33px;margin-top:10px}
.reviews .lead{margin-top:12px}
.review-grid{display:flex;gap:18px;margin:30px 100px 0}
.review{width:322px;height:200px;background:var(--white);border-radius:4px;padding:16px 12px;position:relative;box-shadow:0 2px 8px rgba(0,0,0,.06)}
.stars{color:var(--gold);font-size:13px;letter-spacing:1px}
.review p{font-size:9.5px;line-height:18px;color:#555;margin-top:6px}
.reviewer{display:flex;align-items:center;gap:10px;margin-top:8px}
.avatar{width:36px;height:36px;border-radius:50%;background:linear-gradient(135deg,#c9b29c,#8a9fb6)}
.reviewer b{display:block;font-size:12px;font-weight:600}
.reviewer span{font-size:10px;color:#8a8a8a}
.quote{position:absolute;right:22px;bottom:24px;width:36px;height:28px}
.reviews .center .btn{margin-top:34px;width:204px;height:34px}

/* more than storage */
.more{height:568px}
.more-body{position:absolute;left:100px;top:90px}
.more-body h2{font-size:33px;margin-top:8px}
.checks{list-style:none;margin-top:14px}
.checks li{display:flex;align-items:center;gap:10px;font-size:11px;height:29px;color:#222}
.checks svg{width:14px;height:10px;flex:none}
.more-photo{position:absolute;left:600px;top:60px;width:500px;height:440px;border-radius:4px;background:linear-gradient(180deg,#a7a29a 0%,#7d7367 45%,#8f8f8c 70%,#6f6c68 100%)}

/* reserve */
.reserve{height:294px;background:linear-gradient(180deg,#1d4e9e,#0f3d8c);color:var(--white);padding-top:60px}
.reserve .eyebrow{color:#dfe8f7}
.reserve h2{color:var(--white);font-size:33px;margin-top:10px}
.reserve .lead{color:#e8eef9;margin-top:12px}
.reserve .pair{margin-top:30px}
.reserve .btn-outline{border-color:#c7d6ee}

/* gallery */
.gallery{height:814px;padding-top:66px}
.gallery h2{font-size:33px;margin-top:10px}
.gallery .lead{margin-top:8px}
.tiles{display:grid;grid-template-columns:repeat(3,323px);gap:22px 16px;margin:22px 100px 0}
.tile{height:244px;border-radius:3px}
.gallery .center .btn{margin-top:28px;width:166px;height:34px}

/* contact */
.contact{height:512px;background:var(--pale)}
.contact-body{position:absolute;left:100px;top:68px;width:476px}
.contact-body .eyebrow{font-size:15px}
.contact-body h2{font-size:33px;margin-top:16px}
.form{display:grid;grid-template-columns:1fr 1fr;gap:14px 20px;margin-top:22px}
.field{height:36px;background:var(--white);border:1px solid var(--line);font-size:9px;color:#888;padding:12px 14px}
.field.wide{grid-column:1/3;height:120px}
.contact-body .btn{margin-top:32px;height:30px;width:112px;padding:0}
.contact-photo{position:absolute;left:620px;top:0;width:580px;height:512px;background:linear-gradient(135deg,#e9eef6 0%,#c9d5e6 45%,#5b7fb4 75%,#d8dee8 100%)}

/* footer */
.footer{height:291px}
.foot-brand{position:absolute;left:100px;top:46px}
.foot-brand .brand{font-size:15px}
.foot-brand p{font-size:10.5px;line-height:17px;color:#333;margin-top:40px;width:260px}
.foot-col{position:absolute;top:44px}
.foot-col h4{font-family:"Bebas Neue",sans-serif;font-weight:400;font-size:17px;letter-spacing:.5px}
.links{list-style:none;margin-top:12px}
.links li{font-size:10.5px;height:27px;color:#333}
.info{margin-top:16px}
.info div{display:flex;gap:12px;align-items:flex-start;font-size:10.5px;line-height:16px;margin-bottom:18px;color:#333}
.info i{width:24px;height:24px;border-radius:50%;background:var(--gold);flex:none;display:flex;align-items:center;justify-content:center}
.info svg{width:12px;height:12px}
.subscribe .field{width:228px;margin-top:16px;font-size:9px;height:36px}
.subscribe .btn{width:228px;height:32px;margin-top:14px;text-transform:uppercase;font-weight:600;font-size:10px}
.rule{position:absolute;left:100px;right:100px;top:232px;border-top:1px solid #999}
.copyright{position:absolute;top:256px;left:0;right:0;text-align:center;font-size:11px;color:#333}
</style>
</head>
<body>

<div class="topbar">We Are Available for you <span class="accent">📞</span> Call now : <b>(555) 014-2680</b></div>
<header class="nav">
  <div class="brand"><span class="brand-mark"></span>TidePost</div>
  <nav class="nav-links">
    <span class="on">Home</span><span>Services</span><span>About Us</span><span>Amenities</span><span>Pricing</span><span>Gallery</span>
  </nav>
  <span class="btn btn-gold">Contact Us</span>
</header>

<section class="hero">
  <div class="hero-photo" role="img" aria-label="White sport fishing boat cruising on open water under a stormy sky"></div>
  <div class="dots"><span></span><span></span><span class="on"></span></div>
  <div class="hero-body">
    <div class="eyebrow">Welcome To TidePost Affordable Self Storage</div>
    <h1 class="display">Secure and Accessible<br>RV, Boat, and Auto Storage.</h1>
    <p>Your trusted storage solution with 24/7 monitoring and easy access."</p>
    <div class="actions"><span class="btn btn-gold" style="width:164px">See Availability</span><span class="btn btn-outline">Contact For A Free Quote</span></div>
  </div>
</section>

<section class="why center">
  <div class="eyebrow">Features And Amenities</div>
  <h2 class="display">Why Choose TidePost?</h2>
  <p class="lead">we believe that storage isn't just about clean units at affordable prices. We have the<br>convenient features and amenities that make your move as simple as possible.</p>
  <div class="features">
    <div class="feature">
      <svg viewBox="0 0 36 36"><rect x="5" y="8" width="24" height="17" rx="2" fill="none" stroke="#0f3d8c" stroke-width="2"/><circle cx="17" cy="16" r="4" fill="#f6b21b"/><path d="M12 30h12M18 25v5" stroke="#0f3d8c" stroke-width="2"/></svg>
      <h3>24/7 Security<br>Monitoring</h3>
      <p>State-of-the-art surveillance ensures your vehicles are protected around the clock.</p>
    </div>
    <div class="feature">
      <svg viewBox="0 0 36 36"><circle cx="14" cy="13" r="7" fill="#f6b21b"/><rect x="20" y="6" width="6" height="20" rx="3" fill="none" stroke="#0f3d8c" stroke-width="2"/><circle cx="23" cy="28" r="4" fill="none" stroke="#0f3d8c" stroke-width="2"/></svg>
      <h3>Climate-<br>Controlled Units</h3>
      <p>State-of-the-art surveillance ensures your vehicles are protected around the clock.</p>
    </div>
    <div class="feature">
      <svg viewBox="0 0 36 36"><circle cx="10" cy="14" r="7" fill="#f6b21b"/><rect x="8" y="8" width="22" height="22" rx="2" fill="none" stroke="#0f3d8c" stroke-width="2"/><path d="M8 14h22M12 19h3M17 19h3M22 19h3M12 24h3M17 24h3M22 24h3" stroke="#0f3d8c" stroke-width="2"/></svg>
      <h3>Easy Online<br>Reservations</h3>
      <p>State-of-the-art surveillance ensures your vehicles are protected around the clock.</p>
    </div>
    <div class="feature">
      <svg viewBox="0 0 36 36"><circle cx="18" cy="15" r="6" fill="#f6b21b"/><path d="M6 30V8M30 30V8M6 12h24M6 22h24M12 12v18M18 12v18M24 12v18" stroke="#0f3d8c" stroke-width="2" fill="none"/></svg>
      <h3>Wide Access<br>Gates</h3>
      <p>State-of-the-art surveillance ensures your vehicles are protected around the clock.</p>
    </div>
    <div class="feature">
      <svg viewBox="0 0 36 36"><circle cx="18" cy="13" r="8" fill="#f6b21b"/><path d="M6 14l12-8 12 8v16H6z" fill="none" stroke="#0f3d8c" stroke-width="2"/><rect x="12" y="20" width="12" height="6" fill="none" stroke="#0f3d8c" stroke-width="2"/></svg>
      <h3>Truck<br>Rentals</h3>
      <p>State-of-the-art surveillance ensures your vehicles are protected around the clock.</p>
    </div>
  </div>
</section>

<section class="about">
  <div class="about-photo" role="img" aria-label="Motorhome parked in a pine forest clearing with mountains behind"></div>
  <div class="about-body">
    <div class="eyebrow" style="font-size:11px">ABOUT ON TIDEPOST</div>
    <h2 class="display">Who We Are</h2>
    <p>At TidePost, we specialize in providing safe, reliable, and accessible storage solutions for RVs, boats, and vehicles of all sizes. With state-of-the-art security and a customer-first approach, we make it easy for you to store with confidence.</p>
    <p>It has survived not only five centuries, but also the leap into electronic typesetting, remaining essentially unchanged. It was popularised in the 1960s with the release of Typeleaf sheets containing Lorem Ipsum passages, and more recently with desktop publishing software like Quillset Layout including versions of Lorem Ipsum</p>
    <span class="btn btn-navy">Learn More About Us</span>
  </div>
</section>

<section class="services center">
  <div class="eyebrow">Features And Amenities</div>
  <h2 class="display">Our TidePost Services</h2>
  <p class="lead">we believe that storage isn't just about clean units at affordable prices. We have the<br>convenient features and amenities that make your move as simple as possible.</p>
  <div class="service-grid">
    <div class="service">
      <div class="photo" role="img" aria-label="Large motorhome parked under oak trees" style="background:linear-gradient(180deg,#6f7a66,#9a9584 55%,#5b5d52)"></div>
      <h3>RV Storage</h3>
      <p>Lorem Ipsum has been the industry's standard dummy text ever since the 1500s, when an unknown printer took a galley of type and scrambled it to make a type specimen book.</p>
    </div>
    <div class="service">
      <div class="photo" role="img" aria-label="White motor boat on calm blue water" style="background:linear-gradient(180deg,#8fa6bd,#c9d6e2 50%,#4f7aa3)"></div>
      <h3>Boat Storage</h3>
      <p>Lorem Ipsum has been the industry's standard dummy text ever since the 1500s, when an unknown printer took a galley of type and scrambled it to make a type specimen book.</p>
    </div>
    <div class="service">
      <div class="photo" role="img" aria-label="Red and black sports car in a dark studio" style="background:radial-gradient(ellipse at 60% 60%,#6a1a1e 0%,#2a2a2e 45%,#111 100%)"></div>
      <h3>Auto Storage</h3>
      <p>Lorem Ipsum has been the industry's standard dummy text ever since the 1500s, when an unknown printer took a galley of type and scrambled it to make a type specimen book.</p>
    </div>
  </div>
  <div class="pair"><span class="btn btn-gold" style="width:164px">See Availability</span><span class="btn btn-navy">Contact For A Free Quote</span></div>
</section>

<section class="reviews center">
  <div class="eyebrow" style="font-size:11px">REVIEW</div>
  <h2 class="display">What Our Customers Say</h2>
  <p class="lead">Lorem Ipsum has been the industry's standard dummy text ever since the 1500s, when an<br>unknown printer took a galley of type and scrambled it to make a type specimen book</p>
  <div class="review-grid" style="text-align:left">
    <div class="review">
      <div class="stars">★★★★★</div>
      <p>Lorem Ipsum has been the industry's standard dummy text ever since the 1500s, when an unknown printer took Lorem Ipsum has been the industry's standard dummy text ever since the 1500s, when an unknown printer took a galley of type and scrambled it to make a type specimen book.</p>
      <div class="reviewer"><div class="avatar" role="img" aria-label="Customer portrait"></div><div><b>Mara Ellison</b><span>Lorem Ipsum</span></div></div>
      <svg class="quote" viewBox="0 0 36 28"><path d="M0 28V14C0 5 5 0 14 0v6c-5 0-7 3-7 8h7v14zM20 28V14C20 5 25 0 34 0v6c-5 0-7 3-7 8h7v14z" fill="#0f3d8c"/></svg>
    </div>
    <div class="review">
      <div class="stars">★★★★★</div>
      <p>Lorem Ipsum has been the industry's standard dummy text ever since the 1500s, when an unknown printer took Lorem Ipsum has been the industry's standard dummy text ever since the 1500s, when an unknown printer took a galley of type and scrambled it to make a type specimen book.</p>
      <div class="reviewer"><div class="avatar" role="img" aria-label="Customer portrait"></div><div><b>Mara Ellison</b><span>Lorem Ipsum</span></div></div>
      <svg class="quote" viewBox="0 0 36 28"><path d="M0 28V14C0 5 5 0 14 0v6c-5 0-7 3-7 8h7v14zM20 28V14C20 5 25 0 34 0v6c-5 0-7 3-7 8h7v14z" fill="#0f3d8c"/></svg>
    </div>
    <div class="review">
      <div class="stars">★★★★★</div>
      <p>Lorem Ipsum has been the industry's standard dummy text ever since the 1500s, when an unknown printer took Lorem Ipsum has been the industry's standard dummy text ever since the 1500s, when an unknown printer took a galley of type and scrambled it to make a type specimen book.</p>
      <div class="reviewer"><div class="avatar" role="img" aria-label="Customer portrait"></div><div><b>Mara Ellison</b><span>Lorem Ipsum</span></div></div>
      <svg class="quote" viewBox="0 0 36 28"><path d="M0 28V14C0 5 5 0 14 0v6c-5 0-7 3-7 8h7v14zM20 28V14C20 5 25 0 34 0v6c-5 0-7 3-7 8h7v14z" fill="#0f3d8c"/></svg>
    </div>
  </div>
  <div class="center"><span class="btn btn-navy">View All Review</span></div>
</section>

<section class="more">
  <div class="more-body">
    <div class="eyebrow">Affordable Self Storage</div>
    <h2 class="display">More Than Just A Storage Complex.</h2>
    <ul class="checks">
      <li><svg viewBox="0 0 14 10"><path d="M1 5l4 4 8-8" stroke="#f6b21b" stroke-width="2" fill="none"/></svg>Gated, secure, private, and convenient.</li>
      <li><svg viewBox="0 0 14 10"><path d="M1 5l4 4 8-8" stroke="#f6b21b" stroke-width="2" fill="none"/></svg>24' above sea level.</li>
      <li><svg viewBox="0 0 14 10"><path d="M1 5l4 4 8-8" stroke="#f6b21b" stroke-width="2" fill="none"/></svg>No leaks, flooding, or power loss during Hurricane Irma and Ian.</li>
      <li><svg viewBox="0 0 14 10"><path d="M1 5l4 4 8-8" stroke="#f6b21b" stroke-width="2" fill="none"/></svg>Security cameras.</li>
      <li><svg viewBox="0 0 14 10"><path d="M1 5l4 4 8-8" stroke="#f6b21b" stroke-width="2" fill="none"/></svg>An eight feet high perimeter fence.</li>
      <li><svg viewBox="0 0 14 10"><path d="M1 5l4 4 8-8" stroke="#f6b21b" stroke-width="2" fill="none"/></svg>Motorized and insulated garage door. Oversized: 12' x 14' to 20' x 14'.</li>
      <li><svg viewBox="0 0 14 10"><path d="M1 5l4 4 8-8" stroke="#f6b21b" stroke-width="2" fill="none"/></svg>Air conditioning option.</li>
      <li><svg viewBox="0 0 14 10"><path d="M1 5l4 4 8-8" stroke="#f6b21b" stroke-width="2" fill="none"/></svg>18'+ clear height inside every unit.</li>
      <li><svg viewBox="0 0 14 10"><path d="M1 5l4 4 8-8" stroke="#f6b21b" stroke-width="2" fill="none"/></svg>Fire sprinklers throughout.</li>
      <li><svg viewBox="0 0 14 10"><path d="M1 5l4 4 8-8" stroke="#f6b21b" stroke-width="2" fill="none"/></svg>Concrete block construction.</li>
      <li><svg viewBox="0 0 14 10"><path d="M1 5l4 4 8-8" stroke="#f6b21b" stroke-width="2" fill="none"/></svg>Spotless restrooms, showers, and laundry facility.</li>
    </ul>
  </div>
  <div class="more-photo" role="img" aria-label="Vintage travel trailer parked beside a concrete storage building"></div>
</section>

<section class="reserve center">
  <div class="eyebrow">Get In Touch</div>
  <h2 class="display">Reserve Your Spot Today</h2>
  <p class="lead">Lorem Ipsum has been the industry's standard dummy text ever since the 1500s, when an<br>unknown printer took a galley of type and scrambled it to make a type specimen book</p>
  <div class="pair"><span class="btn btn-gold">Reserve Your Spot Now.</span><span class="btn btn-outline">Contact For A Free Quote</span></div>
</section>

<section class="gallery center">
  <div class="eyebrow">Gallery</div>
  <h2 class="display">See Our Gallery</h2>
  <p class="lead">Explore our secure and well-maintained storage spaces.</p>
  <div class="tiles">
    <div class="tile" role="img" aria-label="Boat bow moored at a dock" style="background:linear-gradient(180deg,#8c9aa8,#c7ced6 50%,#3b4550)"></div>
    <div class="tile" role="img" aria-label="Camper van in a desert landscape" style="background:linear-gradient(180deg,#9aa6ad,#b39978 40%,#8d7458)"></div>
    <div class="tile" role="img" aria-label="Motorhome on a highway at sunset" style="background:linear-gradient(135deg,#3d4756,#c9a56a 50%,#2d3440)"></div>
    <div class="tile" role="img" aria-label="Classic motorhome parked under a blue sky" style="background:linear-gradient(180deg,#9fc0e0,#dfe4e4 55%,#7b7462)"></div>
    <div class="tile" role="img" aria-label="Modern storage building with open bay doors" style="background:linear-gradient(180deg,#5d8fc9,#dfe6ee 50%,#8e949a)"></div>
    <div class="tile" role="img" aria-label="Marina with yachts on blue water" style="background:linear-gradient(180deg,#5a8bc0,#c6d3df 45%,#1f5f94)"></div>
  </div>
  <div class="center"><span class="btn btn-navy">View All</span></div>
</section>

<section class="contact">
  <div class="contact-body">
    <div class="eyebrow">Get In Touch</div>
    <h2 class="display">Contact With Us</h2>
    <div class="form">
      <div class="field">First Name</div><div class="field">Last Name</div>
      <div class="field">Email</div><div class="field">Phone</div>
      <div class="field wide">Message</div>
    </div>
    <span class="btn btn-navy" style="font-weight:600;font-size:9.5px">Submit Now</span>
  </div>
  <div class="contact-photo" role="img" aria-label="Support agent with headset working at a laptop"></div>
</section>

<footer class="footer">
  <div class="foot-brand">
    <div class="brand"><span class="brand-mark"></span>TidePost</div>
    <p>Lorem Ipsum has been the industry's standard dummy text ever since the 1500s, when an unknown printer took a galley of type and scrambled it to make a type specimen book</p>
  </div>
  <div class="foot-col" style="left:441px">
    <h4>Quick Links</h4>
    <ul class="links"><li>Services</li><li>About Us</li><li>Amenities</li><li>Pricing</li><li>Gallery</li></ul>
  </div>
  <div class="foot-col" style="left:594px">
    <h4>Contact Info</h4>
    <div class="info">
      <div><i><svg viewBox="0 0 12 12"><path d="M2 1l2 0 1 3-1.5 1a6 6 0 003 3L8 7l3 1v2c0 1-1 1-1 1A9 9 0 011 2c0 0 0-1 1-1z" fill="#fff"/></svg></i><span style="padding-top:4px">555-014-2681</span></div>
      <div><i><svg viewBox="0 0 12 12"><rect x="1" y="2.5" width="10" height="7" fill="none" stroke="#fff" stroke-width="1.3"/><path d="M1 3l5 4 5-4" stroke="#fff" stroke-width="1.3" fill="none"/></svg></i><span style="padding-top:4px">info@tidepost.example</span></div>
      <div><i><svg viewBox="0 0 12 12"><path d="M6 11S2 7 2 4.5a4 4 0 018 0C10 7 6 11 6 11z" fill="#fff"/><circle cx="6" cy="4.5" r="1.4" fill="#f6b21b"/></svg></i><span>Lorem Ipsum is simply dummy<br>industry. 48 Harbor Row, Suite 2</span></div>
    </div>
  </div>
  <div class="foot-col subscribe" style="left:874px">
    <h4>Subscribe Newsletter</h4>
    <div class="field">Email</div>
    <span class="btn btn-navy">Subscribe</span>
  </div>
  <div class="rule"></div>
  <div class="copyright">© Copyright All Right Reserved.2024</div>
</footer>

</body>
</html>
```